flyer for CAR REPAIR GARAGE

Kestrel Auto requires a flyer for this new company.We are a MOT vehicle testing station and auto repair garage based in Ashmoor, Wexley.
Our clients can expect quality service at competitive prices.
We provide:
MOT's Class 4, 5, 7 While you wait
Exhaust
Brakes
Suspensions
Clutches
Tyres
Services
For car and commercial

MOT from £39.95
Free Health Check with every MOT

Target Market(s)

Anyone with a car

Industry/Entity Type

Car Repair

Font styles to use
Sans Serif

Colors
ffc214
0455a3
f37122
ec1f27

Requirements
Must have
• The following information:
• Company: Kestrel Auto
• Location: 14 Penbury Lane, (corner of) Hollowmere Street, Ashmoor, Wexley, RM14 7QD
• Telephone: 020 8463 2918
• Mobile: 07812 455 639
• Also to include the following text :
• MOT's Class 4, 5, 7 While you wait
• Exhaust
• Brakes
• Suspensions
• Clutches
• Tyres
• Services
• For car and commercial
• MOT from £39.95
• Free Health Check with every MOT
• Opening times:
• Mon - Sat 0800 - 1900
• Sun 1000 - 1600
Nice to have
• high quality images of car/repair/garage related to company service
• Clean bold lines

```html
<!DOCTYPE html>
<html lang="en">
<head>
<meta charset="utf-8">
<title>Kestrel Auto – MOT Testing Station Flyer</title>
<link rel="stylesheet" href="https://fonts.googleapis.com/css2?family=Arimo:ital,wght@0,400;0,700;1,700&display=swap">
<style>
  :root {
    --yellow: #ffc214;
    --blue: #0455a3;
    --blue-deep: #043d7a;
    --orange: #f37122;
    --red: #ec1f27;
    --white: #ffffff;
    --ink: #1d2a3a;
    --grey: #5a6470;
  }
  * { box-sizing: border-box; margin: 0; padding: 0; }
  html, body { width: 900px; height: 1200px; overflow: hidden; background: #eeeeee; }
  body { font-family: "Arimo", Arial, sans-serif; }
  .flyer { position: relative; width: 900px; height: 1200px; background: var(--white); overflow: hidden; }

  .header { position: absolute; left: 0; top: 0; width: 900px; height: 150px; padding: 32px 40px 0; }
  .headline { color: var(--blue); font-weight: 700; font-size: 46px; line-height: 1.1; }

  .hero-photo { position: absolute; left: 0; top: 150px; width: 900px; height: 430px;
    background: linear-gradient(120deg, #c9d6e4 0%, #8ea2b8 35%, #2a3440 60%, #6c7888 100%); }

  .badge { position: absolute; }
  .badge svg { position: absolute; inset: 0; width: 100%; height: 100%; }
  .badge-text { position: absolute; inset: 0; display: flex; flex-direction: column; align-items: center; justify-content: center; text-align: center; font-weight: 700; }
  .brand-badge { left: 610px; top: 185px; width: 230px; height: 230px; }
  .brand-badge .badge-text { color: var(--ink); font-size: 38px; line-height: 1.1; }

  .tagline-band { position: absolute; left: -20px; top: 560px; width: 940px; height: 62px; background: var(--yellow); transform: skewY(-1.5deg); border-top: 6px solid var(--blue-deep); }
  .tagline { position: absolute; left: 40px; top: 568px; width: 840px; white-space: nowrap; color: var(--blue-deep); font-style: italic; font-weight: 700; font-size: 27px; transform: rotate(-1.5deg); }

  .offer-panel { position: absolute; left: 0; top: 620px; width: 900px; height: 470px; background: linear-gradient(180deg, var(--blue) 0%, var(--blue-deep) 100%); }
  .price { position: absolute; left: 40px; top: 650px; color: var(--white); font-weight: 700; font-size: 52px; }

  .services { position: absolute; left: 40px; top: 738px; width: 300px; }
  .services-label { display: inline-block; background: var(--orange); color: var(--white); font-weight: 700; font-size: 24px; padding: 6px 16px; border-radius: 4px; }
  .service-list { list-style: none; margin-top: 14px; }
  .service-list li { position: relative; padding-left: 30px; color: var(--white); font-size: 19px; line-height: 1.25; margin-bottom: 7px; }
  .service-list li::before { content: ""; position: absolute; left: 0; top: 3px; width: 16px; height: 16px; border-radius: 50%; background: var(--red); border: 2px solid var(--white); }

  .free-badge { left: 355px; top: 730px; width: 215px; height: 215px; }
  .free-badge .badge-text { color: var(--blue-deep); font-size: 21px; line-height: 1.15; padding: 0 42px; }
  .free-badge .free { color: var(--red); font-size: 40px; }

  .hours { position: absolute; left: 340px; top: 962px; width: 250px; text-align: center; }
  .hours-title { color: var(--yellow); font-weight: 700; font-size: 26px; margin-bottom: 8px; white-space: nowrap; }
  .hours p { color: var(--white); font-size: 19px; line-height: 1.45; white-space: nowrap; }

  .service-photo { position: absolute; left: 595px; width: 270px; height: 165px; border: 4px solid var(--white); }
  .service-photo.engine { top: 720px; background: linear-gradient(135deg, #1e2b3c, #5f7a99 60%, #c8d4e0); }
  .service-photo.underbody { top: 900px; background: linear-gradient(135deg, #d9e1ea, #7a8ea6 50%, #243246); }

  .footer { position: absolute; left: 0; top: 1090px; width: 900px; height: 110px; background: linear-gradient(180deg, #ffffff, #e6e9ee); display: flex; align-items: center; padding: 0 40px; }
  .address { color: var(--grey); font-size: 14px; line-height: 1.4; width: 230px; font-style: normal; }
  .contact { color: var(--red); font-weight: 700; font-size: 24px; white-space: nowrap; margin-left: 20px; }
  .contact + .contact { margin-left: 40px; }
</style>
</head>
<body>
<main class="flyer">
  <header class="header">
    <h1 class="headline">MOT vehicle testing station<br>and auto repair garage</h1>
  </header>

  <div class="hero-photo" role="img" aria-label="Mechanic in overalls standing beside a car with its bonnet open"></div>

  <div class="badge brand-badge">
    <svg viewBox="0 0 100 100" aria-hidden="true"><polygon fill="#ffc214" points="100,50 91.2,58.2 96.2,69.1 84.9,73.3 85.4,85.4 73.3,84.9 69.1,96.2 58.2,91.2 50,100 41.8,91.2 30.9,96.2 26.7,84.9 14.6,85.4 15.1,73.3 3.8,69.1 8.8,58.2 0,50 8.8,41.8 3.8,30.9 15.1,26.7 14.6,14.6 26.7,15.1 30.9,3.8 41.8,8.8 50,0 58.2,8.8 69.1,3.8 73.3,15.1 85.4,14.6 84.9,26.7 96.2,30.9 91.2,41.8"/></svg>
    <div class="badge-text"><span>Kestrel</span><span>Auto</span></div>
  </div>

  <div class="offer-panel"></div>
  <div class="tagline-band"></div>
  <p class="tagline">Our clients can expect quality service at competitive prices</p>

  <p class="price">MOT from £39.95</p>

  <section class="services">
    <h2 class="services-label">We provide:</h2>
    <ul class="service-list">
      <li>MOT's Class 4, 5, 7<br>While you wait</li>
      <li>Exhaust</li>
      <li>Brakes</li>
      <li>Suspensions</li>
      <li>Clutches</li>
      <li>Tyres</li>
      <li>Services</li>
      <li>For car and commercial</li>
    </ul>
  </section>

  <div class="badge free-badge">
    <svg viewBox="0 0 100 100" aria-hidden="true"><polygon fill="#ffc214" points="100,50 91.2,58.2 96.2,69.1 84.9,73.3 85.4,85.4 73.3,84.9 69.1,96.2 58.2,91.2 50,100 41.8,91.2 30.9,96.2 26.7,84.9 14.6,85.4 15.1,73.3 3.8,69.1 8.8,58.2 0,50 8.8,41.8 3.8,30.9 15.1,26.7 14.6,14.6 26.7,15.1 30.9,3.8 41.8,8.8 50,0 58.2,8.8 69.1,3.8 73.3,15.1 85.4,14.6 84.9,26.7 96.2,30.9 91.2,41.8"/></svg>
    <div class="badge-text"><span class="free">FREE</span><span>Health Check with every MOT</span></div>
  </div>

  <section class="hours">
    <h2 class="hours-title">Opening Times:</h2>
    <p>Mon to Sat 08:00 - 19:00</p>
    <p>Sun 10:00 - 16:00</p>
  </section>

  <div class="service-photo engine" role="img" aria-label="Mechanic working on a car engine"></div>
  <div class="service-photo underbody" role="img" aria-label="Mechanic repairing the underside of a car"></div>

  <footer class="footer">
    <address class="address">14 Penbury Lane, (corner of)<br>Hollowmere Street,<br>Ashmoor, Wexley, RM14 7QD</address>
    <p class="contact">Tel: 020 8463 2918</p>
    <p class="contact">Mob: 07812 455 639</p>
  </footer>
</main>
</body>
</html>
```